UK Supplement Company Needs a Label for Diet Protein Powder

We need a new, modern and fresh design for our Diet Protein Powder. Our protein powder is packaged in black plastic tubs (photo attached) and needs an attractive label. We would like to see designs that grab attention and look professional. We're very open to ideas. The label should be 88mm x 365mm. We also prefer PSD format where possible. These alterations could be made once your design is chosen. Have attached photo of our shake ingredients/benefits.
Updates

Need extra days to review

Target Market(s)

Slimmers

Industry/Entity Type

Health And Wellness

Font styles to use
Serif
Sans Serif

Colors

Designer to choose colors to be used in the design.

Requirements
Must have
• Clean, Modern and Professional Look. Eye catching. The flavour, we offer 6 flavours so this must be something we can edit (Flavours are Banana, Chocolate, Chocolate Mint, Strawberry, Toffee and Vanilla).
Nice to have
• Our logo, this can be BRISK Nutrition or just BRISK. Our logo files are attached.
Should not have
• We do not want to see people (faces or bodies) on the design.

```html
<!DOCTYPE html>
<html lang="en">
<head>
<meta charset="utf-8">
<title>BRISK Nutrition – Protein Powder Labels</title>
<link href="https://fonts.googleapis.com/css2?family=Oswald:wght@300;400;500&family=Montserrat:wght@700;800;900&display=swap" rel="stylesheet">
<style>
  :root{
    --page:#ffffff;
    --ink:#111111;
    --navy:#0d1b2a;
    --blue:#1f7fc0;
    --blue-light:#56b7e6;
    --blue-pale:#cfe9f7;
    --green:#9cc93b;
    --grey-label:#eeeeee;
    --grey-text:#444444;
    --badge-grey:#8a8a8a;
    --organic:#1e6b35;
    --red:#c0262d;
    --berry:#d8343a;
    --berry-dark:#a8222a;
  }
  *{box-sizing:border-box;margin:0;padding:0}
  html,body{width:1200px;height:800px;overflow:hidden;background:var(--page)}
  body{position:relative;font-family:"Montserrat",sans-serif;color:var(--ink)}

  .sample-title{position:absolute;top:48px;width:490px;text-align:center;
    font-family:"Oswald",sans-serif;font-weight:400;font-size:34px;letter-spacing:4px;color:var(--ink)}
  .sample-title--one{left:70px}
  .sample-title--two{left:640px}

  .label{position:absolute;top:200px;width:490px;height:390px;overflow:hidden;
    background:var(--grey-label);box-shadow:0 4px 18px rgba(0,0,0,.12)}
  .label--one{left:70px;background:#f3f3f3}
  .label--two{left:640px;background:linear-gradient(90deg,#e9e9e9,#f6f6f6 60%,#ececec)}
  .label__bg{position:absolute;inset:0}

  .diet-tag{position:absolute;bottom:20px;transform-origin:left bottom;transform:rotate(-90deg);
    font-family:"Oswald",sans-serif;font-weight:400;white-space:nowrap}
  .label--one .diet-tag{color:#fff;font-size:19px;letter-spacing:6px;left:46px}
  .label--two .diet-tag{color:var(--grey-text);font-size:12px;letter-spacing:2px;left:62px;bottom:160px}

  .brand{position:absolute;top:28px;display:flex;align-items:center;gap:10px}
  .label--one .brand{left:72px}
  .label--two .brand{left:92px}
  .brand__seal{width:48px;height:48px;border-radius:50%;background:var(--badge-grey);border:3px solid #fff;flex:none}
  .brand__name{font-family:"Montserrat",sans-serif;font-weight:800;font-size:21px;color:var(--blue-light);line-height:1;white-space:nowrap}

  .product-name{position:absolute;left:80px;font-family:"Montserrat",sans-serif;font-weight:900;line-height:1;white-space:nowrap}
  .product-name--protein{top:105px;font-size:66px;letter-spacing:-1px}
  .label--one .product-name--protein{color:#fff}
  .label--two .product-name--protein{background:linear-gradient(90deg,var(--blue),#2a5d9b);
    -webkit-background-clip:text;background-clip:text;color:transparent}
  .product-name--powder{top:190px;font-size:48px;color:var(--green)}
  .label--two .product-name--powder{top:183px}

  .divider{position:absolute;left:80px;top:245px;width:250px;height:3px;
    background:linear-gradient(90deg,var(--green),var(--blue) 55%,var(--green))}

  .claims{position:absolute;left:88px;top:252px;width:240px;border-left:2px solid var(--green);padding-left:6px}
  .claims__sub{font-family:"Oswald",sans-serif;font-weight:300;font-size:17px;color:var(--grey-text);line-height:1.2;white-space:nowrap}
  .claims__main{font-family:"Oswald",sans-serif;font-weight:500;font-size:19px;color:var(--ink);line-height:1.2;white-space:nowrap}
  .claims__free{font-family:"Montserrat",sans-serif;font-weight:700;font-size:5px;color:#666;letter-spacing:.1px;margin-top:4px;white-space:nowrap}

  .stats{position:absolute;left:88px;top:318px;display:flex;gap:11px}
  .stat{width:46px;height:46px;border-radius:50%;background:var(--blue-light);color:#fff;text-align:center;
    display:flex;flex-direction:column;justify-content:center;font-family:"Oswald",sans-serif;line-height:1}
  .stat__value{font-size:14px;font-weight:500}
  .stat__unit{font-size:5.5px;font-weight:400;margin-top:2px}
  .stat--badge{background:#fff;border:4px solid var(--organic)}

  .net-weight{position:absolute;left:88px;top:370px;font-family:"Oswald",sans-serif;font-weight:400;font-size:13px;color:var(--ink)}

  .flavour-art{position:absolute;left:342px;top:228px;width:112px;height:112px;border-radius:50%;
    background:radial-gradient(circle at 45% 45%,var(--berry),var(--berry-dark))}
  .flavour-tag{position:absolute;left:326px;top:362px;background:var(--red);color:#fff;border-radius:10px;
    padding:3px 12px;font-family:"Oswald",sans-serif;font-weight:400;font-size:10.5px;letter-spacing:.3px;white-space:nowrap}
</style>
</head>
<body>

<h2 class="sample-title sample-title--one">SAMPLE ONE</h2>
<h2 class="sample-title sample-title--two">SAMPLE TWO</h2>

<section class="label label--one">
  <svg class="label__bg" viewBox="0 0 490 390" width="490" height="390" aria-hidden="true">
    <defs>
      <linearGradient id="bandShade" x1="0" y1="0" x2="1" y2="0">
        <stop offset="0" stop-color="#0d4f86"/><stop offset="1" stop-color="#56b7e6"/>
      </linearGradient>
    </defs>
    <path d="M0 0 H470 V160 Q470 178 452 178 H92 Q75 178 75 195 V360 Q75 378 58 380 L0 390 Z" fill="#2a86c4"/>
    <path d="M0 0 H470 V160 Q470 178 452 178 H92 Q75 178 75 195 V360 L0 390 Z" fill="url(#bandShade)" opacity=".35"/>
    <path d="M28 0 H345 V82 Q345 98 329 98 H28 Z" fill="var(--navy)"/>
  </svg>
  <div class="diet-tag">LOW CALORIE DIET</div>
  <div class="brand"><span class="brand__seal"></span><span class="brand__name">BRISK Nutrition</span></div>
  <div class="product-name product-name--protein">PROTEIN</div>
  <div class="product-name product-name--powder">POWDER</div>
  <div class="claims">
    <p class="claims__sub">Dietary Supplement</p>
    <p class="claims__main">SUPER ADVANCED FORMULA</p>
    <p class="claims__free">SOY FREE &nbsp;|&nbsp; DAIRY FREE &nbsp;|&nbsp; GLUTEN FREE &nbsp;|&nbsp; NON GMO &nbsp;|&nbsp; NO ADDED SUGAR</p>
  </div>
  <div class="stats">
    <div class="stat"><span class="stat__value">117</span><span class="stat__unit">CALORIES<br>PER SERVING</span></div>
    <div class="stat"><span class="stat__value">4.2</span><span class="stat__unit">CARBS<br>PER SERVING</span></div>
    <div class="stat"><span class="stat__value">21G</span><span class="stat__unit">PROTEIN<br>PER SERVING</span></div>
    <div class="stat stat--badge"></div>
  </div>
  <div class="net-weight">NET WT. 600G</div>
  <div class="flavour-art" role="img" aria-label="Fresh strawberries with leaves"></div>
  <div class="flavour-tag">STRAWBERRY FLAVOUR</div>
</section>

<section class="label label--two">
  <svg class="label__bg" viewBox="0 0 490 390" width="490" height="390" aria-hidden="true">
    <defs>
      <linearGradient id="edgeBlue" x1="0" y1="0" x2="1" y2="0">
        <stop offset="0" stop-color="#7cc7ec"/><stop offset="1" stop-color="#3aa4dd"/>
      </linearGradient>
    </defs>
    <path d="M0 0 H62 Q30 120 46 230 Q58 320 100 390 H0 Z" fill="url(#edgeBlue)"/>
    <path d="M62 0 Q38 120 54 230 Q66 320 110 390" fill="none" stroke="var(--blue-pale)" stroke-width="6"/>
    <path d="M70 0 Q46 120 62 230 Q74 320 118 390" fill="none" stroke="#bfe2f4" stroke-width="2"/>
  </svg>
  <div class="diet-tag">LOW CALORIE DIET</div>
  <div class="brand"><span class="brand__seal"></span><span class="brand__name">BRISK Nutrition</span></div>
  <div class="product-name product-name--protein">PROTEIN</div>
  <div class="product-name product-name--powder">POWDER</div>
  <div class="divider"></div>
  <div class="claims">
    <p class="claims__sub">Dietary Supplement</p>
    <p class="claims__main">SUPER ADVANCED FORMULA</p>
    <p class="claims__free">SOY FREE &nbsp;|&nbsp; DAIRY FREE &nbsp;|&nbsp; GLUTEN FREE &nbsp;|&nbsp; NON GMO &nbsp;|&nbsp; NO ADDED SUGAR</p>
  </div>
  <div class="stats">
    <div class="stat"><span class="stat__value">117</span><span class="stat__unit">CALORIES<br>PER SERVING</span></div>
    <div class="stat"><span class="stat__value">4.2</span><span class="stat__unit">CARBS<br>PER SERVING</span></div>
    <div class="stat"><span class="stat__value">21G</span><span class="stat__unit">PROTEIN<br>PER SERVING</span></div>
    <div class="stat stat--badge"></div>
  </div>
  <div class="net-weight">NET WT. 600G</div>
  <div class="flavour-art" role="img" aria-label="Fresh strawberries with leaves"></div>
  <div class="flavour-tag">STRAWBERRY FLAVOUR</div>
</section>

</body>
</html>
```